Design a DJ Biography Page.

Looking for a designer to design my DJ Bio page with the text I have provided , & the logo and some photos incorporated into the Bio design. Looking for a modern nightclub style design, possibly white lettering on a dark background. Use a crowd scene photo as the cover photo , then incorporate smaller photos along the side of the bio. Please print the bio in distinct paragraphs & do no edit the wording please, The Bio text reads as follows - DJ Drifter (a.k.a Lewis Tamberly) is an intuitive, creative open format DJ with a distinct urban flavour. His unique energetic performances seamlessly transition through different genres. He reads crowds & presents fresh dynamic sets, that tell a story . His freestyle sets create an uplifting dancefloor experience. DJ Drifters top achievement too date, is through the word of mouth reputation of his sets , transforming a quiet café/bar into a thriving premier nightclub party destination, with capacity crowds of 400 people , packed dancefloors & an entry line up every Saturday night when DJ Drifter performs one of his weekly residencies @ Lantern Bar. DJ Drifter is currently resident DJ @ Lantern Bar which is located in the heart of the tropical city of Darwin, capital of Australia's Northern Territory . DJ Drifter performs Friday(10pm-2am) Saturday (10pm-2am) & Sunday nights (RnB session 8pm-2am) each weekend. Lewis Tamberly began his DJ career at Rave events in the early 2000s. In 2008 Lewis adopted the name DJ Drifter & made the transition too become an open format DJ, initially playing @ Opal Reef Casino & Fennigans Bar(Old School Funk set on Friday nights). He also performed at a host of other venues including the Marlow Terrace, The Exhibition hall ,The Belmore Darwin , Zenith Loft, Seabreeze Lodge Foreshore & many more. In October 2009 DJ Drifter emerged onto the Club scene playing 6 hr sets Thurs-Sat nights @ The Velvet Comet Night Club. This was a very popular Club back in 2009 & it was at this venue that DJ Drifter gained much of his initial learning experiences as a Nightclub DJ . He also hosted party games, quiz nights & events such as wet t-shirt comps & Jelly wrestling @ The Velvet Comet night Club. Through these events DJ Drifter developed his top level M.C skills. By October 2010 DJ Drifter began DJ residencies at five different venues each week, these included - Wed Nights @ The Kelby Creek Tavern -Thurs Nights @ Velvet Comet Night Club - Fri Nights @ Murphys Clover Bar (7pm-11pm) & Fri Nights @ Parrot Perch Bar (12pm-2am) - Sat Nights @ Lantern Bar- Sun Nights @ Murphys Clover Bar. DJ Drifter also had the experience of playing too larger 1000 plus people crowds at the outdoor events "Bluestone Beats 2012" & at a 2011 "Street Party" for Murphys Bar's 15th Birthday Party . In 2013 DJ Drifter became the exclusive resident DJ @ Lantern Bar. This venue gave him the maximum creative freedom he needed , to be able to develop his signature DJ sets. He initially performed @ Lantern Bar Fri & Sat nights in 2013, the following year he expanded to 3 nights per week playing a Throwbacks set on a Thursday night. Early 2016 saw the launch of DJ Drifters RnB Brand "The Velvet Vintage Series" which rapidly became Darwin's biggest weekly Sunday night session attracting a regular loyal following. DJ Drifters future aspirations are to reach a wider audience by taking his DJ performances to International & Interstate venues . He is currently working hard in the studio creating original tracks as wells as remixes, mash-ups , mix tapes & pod casts. DJ Drifter is a guaranteed party starter for mainstream venues & events.

```html
<!DOCTYPE html>
<html lang="en">
<head>
<meta charset="utf-8">
<title>DJ Drifter – Biography</title>
<link rel="stylesheet" href="https://fonts.googleapis.com/css2?family=Arimo:wght@400;700&display=swap">
<style>
  :root {
    --page-bg: #000000;
    --text: #ffffff;
    --crowd-skin: #b0704f;
    --crowd-shadow: #2a1a1e;
    --stage-red: #c02a48;
    --stage-amber: #d08a3a;
    --light-blue: #3f6fe0;
    --light-cyan: #7fc8ff;
    --haze-purple: #6a3fa0;
    --decks-dark: #0b0d16;
    --suit-grey: #4a4c58;
    --studio-teal: #2f5a66;
    --band-pink: #c8306e;
    --band-violet: #5a2a8a;
    --band-blue: #2050ff;
    --spark-blue: rgba(60, 110, 255, 0.22);
  }
  * { margin: 0; padding: 0; box-sizing: border-box; }
  html, body { width: 848px; height: 1200px; overflow: hidden; background: var(--page-bg); }
  .bio-page {
    position: relative; width: 848px; height: 1200px; overflow: hidden;
    color: var(--text);
    font-family: "Arimo", Arial, sans-serif;
    background:
      radial-gradient(ellipse 160px 60px at 120px 780px, var(--spark-blue), transparent 70%),
      radial-gradient(ellipse 200px 50px at 700px 890px, var(--spark-blue), transparent 70%),
      radial-gradient(ellipse 180px 60px at 300px 930px, var(--spark-blue), transparent 70%),
      var(--page-bg);
  }
  .cover-photo {
    position: absolute; left: 0; top: 0; width: 848px; height: 424px;
    background:
      radial-gradient(ellipse 150px 130px at 690px 200px, var(--crowd-skin), transparent 70%),
      radial-gradient(ellipse 200px 110px at 720px 60px, var(--stage-red), transparent 70%),
      radial-gradient(ellipse 110px 160px at 800px 260px, var(--light-blue), transparent 70%),
      radial-gradient(ellipse 160px 150px at 80px 120px, var(--crowd-skin), transparent 72%),
      radial-gradient(ellipse 130px 120px at 470px 130px, var(--stage-amber), transparent 72%),
      radial-gradient(ellipse 300px 150px at 290px 150px, var(--haze-purple), transparent 75%),
      radial-gradient(ellipse 340px 90px at 330px 370px, var(--light-cyan), transparent 70%),
      linear-gradient(180deg, var(--crowd-shadow) 0%, #1a1430 60%, var(--decks-dark) 100%);
  }
  .brand-name {
    position: absolute; left: 100px; top: 30px;
    font-family: "Arimo", Arial, sans-serif; font-weight: 700;
    font-size: 118px; line-height: 1.0; color: var(--text);
  }
  .inset-photo {
    position: absolute; left: 35px; top: 451px; width: 255px; height: 181px;
    background:
      radial-gradient(ellipse 70px 60px at 175px 60px, var(--crowd-skin), transparent 70%),
      radial-gradient(ellipse 120px 90px at 60px 60px, var(--studio-teal), transparent 75%),
      linear-gradient(160deg, var(--suit-grey), #15161c 80%);
  }
  .bio-text { position: absolute; font-size: 10.5px; line-height: 1.32; }
  .bio-text p + p { margin-top: 5px; }
  .bio-intro { left: 300px; top: 452px; width: 530px; }
  .bio-origins { left: 35px; top: 641px; width: 795px; }
  .bio-clubs { left: 35px; top: 696px; width: 795px; }
  .bio-clubs .centred { text-align: center; }
  .crowd-photo {
    float: right; width: 258px; height: 224px; margin: 0 0 6px 12px;
    background:
      radial-gradient(ellipse 60px 50px at 190px 90px, var(--stage-amber), transparent 70%),
      radial-gradient(ellipse 90px 70px at 70px 130px, var(--crowd-skin), transparent 72%),
      radial-gradient(ellipse 110px 80px at 130px 40px, var(--light-blue), transparent 75%),
      linear-gradient(180deg, #1a1d33, var(--crowd-shadow));
  }
  .bio-future {
    position: absolute; left: 35px; top: 962px; width: 795px;
    font-size: 12.5px; line-height: 1.3;
  }
  .bookings-band {
    position: absolute; left: 0; top: 1016px; width: 848px; height: 184px;
    background:
      radial-gradient(ellipse 90px 30px at 200px 75px, var(--light-cyan), transparent 70%),
      radial-gradient(ellipse 90px 30px at 650px 75px, var(--light-cyan), transparent 70%),
      radial-gradient(ellipse 340px 70px at 424px 75px, var(--band-blue), transparent 75%),
      radial-gradient(ellipse 160px 80px at 90px 130px, var(--crowd-skin), transparent 70%),
      radial-gradient(ellipse 160px 80px at 760px 130px, var(--crowd-skin), transparent 70%),
      linear-gradient(90deg, var(--band-pink), var(--band-violet) 30%, #141040 50%, var(--band-violet) 70%, var(--band-pink));
  }
  .bookings-list {
    position: absolute; left: 0; top: 1030px; width: 848px;
    list-style: none; text-align: center;
    font-size: 12.5px; line-height: 20px; font-weight: 700;
  }
</style>
</head>
<body>
<main class="bio-page">
  <div class="cover-photo" role="img" aria-label="Cover photo: DJ Drifter singing into a microphone behind the decks in front of a packed, cheering nightclub crowd under coloured lights"></div>
  <h1 class="brand-name">DJ<br>Drifter</h1>

  <div class="inset-photo" role="img" aria-label="Photo of DJ Drifter in a suit working the mixing decks"></div>

  <section class="bio-text bio-intro">
    <p>DJ Drifter (a.k.a Lewis Tamberly) is an intuitive, creative open format DJ with a distinct urban flavour. His unique energetic performances seamlessly transition through different genres. He reads crowds &amp; presents fresh dynamic sets, that tell a story . His freestyle sets create an uplifting dancefloor experience.</p>
    <p>DJ Drifters top achievement too date, is through the word of mouth reputation of his sets , transforming a quiet café/bar into a thriving premier nightclub party destination, with capacity crowds of 400 people , packed dancefloors &amp; an entry line up every Saturday night when DJ Drifter performs one of his weekly residencies @ Lantern Bar.</p>
    <p>DJ Drifter is currently resident DJ @ Lantern Bar which is located in the heart of the tropical city of Darwin, capital of Australia's Northern Territory . DJ Drifter performs Friday(10pm-2am) Saturday (10pm-2am) &amp; Sunday nights (RnB session 8pm-2am) each weekend.</p>
  </section>

  <section class="bio-text bio-origins">
    <p>Lewis Tamberly began his DJ career at Rave events in the early 2000s. In 2008 Lewis adopted the name DJ Drifter &amp; made the transition too become an open format DJ, initially playing @ Opal Reef Casino &amp; Fennigans Bar(Old School Funk set on Friday nights). He also performed at a host of other venues including the Marlow Terrace, The Exhibition hall ,The Belmore Darwin , Zenith Loft, Seabreeze Lodge Foreshore &amp; many more.</p>
  </section>

  <section class="bio-text bio-clubs">
    <div class="crowd-photo" role="img" aria-label="Photo of a cheering crowd on the dancefloor"></div>
    <p class="centred">In October 2009 DJ Drifter emerged onto the Club scene playing 6 hr sets Thurs-Sat nights @ The Velvet Comet Night Club. This was a very popular Club back in 2009 &amp; it was at this venue that DJ Drifter gained much of his initial learning experiences as a Nightclub DJ . He also hosted party games, quiz nights &amp; events such as wet t-shirt comps &amp; Jelly wrestling @ The Velvet Comet night Club. Through these events DJ Drifter developed his top level M.C skills.</p>
    <p class="centred">By October 2010 DJ Drifter began DJ residencies at five different venues each week, these included - Wed Nights @ The Kelby Creek Tavern -Thurs Nights @ Velvet Comet Night Club - Fri Nights @ Murphys Clover Bar (7pm-11pm) &amp; Fri Nights @ Parrot Perch Bar (12pm-2am) - Sat Nights @ Lantern Bar- Sun Nights @ Murphys Clover Bar.</p>
    <p>DJ Drifter also had the experience of playing too larger 1000 plus people crowds at the outdoor events "Bluestone Beats 2012" &amp; at a 2011 "Street Party" for Murphys Bar's 15th Birthday Party . In 2013 DJ Drifter became the exclusive resident DJ @ Lantern Bar. This venue gave him the maximum creative freedom he needed , to be able to develop his signature DJ sets. He initially performed @ Lantern Bar Fri &amp; Sat nights in 2013, the following year he expanded to 3 nights per week playing a Throwbacks set on a Thursday night. Early 2016 saw the launch of DJ Drifters RnB Brand "The Velvet Vintage Series" which rapidly became Darwin's biggest weekly Sunday night session attracting a regular loyal following.</p>
  </section>

  <p class="bio-future">DJ Drifters future aspirations are to reach a wider audience by taking his DJ performances to International &amp; Interstate venues . He is currently working hard in the studio creating original tracks as wells as remixes, mash-ups , mix tapes &amp; pod casts. DJ Drifter is a guaranteed party starter for mainstream venues &amp; events.</p>

  <div class="bookings-band" role="img" aria-label="Photo of a crowd with raised hands under pink and blue club lights"></div>
  <ul class="bookings-list">
    <li>Bookings- bookings@drifterdeejays.example</li>
    <li>Snapline- deejaydrifter</li>
    <li>Friendwall - DJ Drifter</li>
    <li>Wavecrate - DJ Drifter</li>
    <li>Setstream - DJ Drifter</li>
    <li>Crate Pool - DJ Drifter</li>
  </ul>
</main>
</body>
</html>
```